Wine Label for a White and a Red Wine from Italy

We have a very good idea of what we want with artwork. We need you to please design a 'template' with the text so we can change out the artwork from year to year. Samples are shown of what we are looking for. We are looking for options with the two basic designs. Brand name of wine is: Valora di Castegno. Both wines are in a light green Bordeaux-style bottle (note: we don't show a light green bottle in the mockup but please remember the bottle is light green). Artwork is provided. We'd like to see either the green or blue butterfly on the white wine, the red butterfly is for the red wine. Please base the design on the attached label from Brailey and/or the attached label from Chateau Mervanges.

Target Market(s)

Millennials, women

Requirements
Must have
• The artwork (butterflies) attached.
Nice to have
• Elegant, readable fonts. Please make the text so it can be changed by the printer. Please make it so the artwork can be changed too.

```html
<!DOCTYPE html>
<html lang="en">
<head>
<meta charset="utf-8">
<title>Valora di Castegno – Label Range</title>
<link rel="stylesheet" href="https://fonts.googleapis.com/css2?family=Playfair+Display:wght@400;500&family=Barlow+Condensed:wght@400;500&display=swap">
<style>
  :root {
    --backdrop: #2d2f2d;
    --paper: #f7f7f5;
    --ink: #2e3236;
    --ink-soft: #4a4f55;
    --leaf: #6f8f2f;
    --leaf-deep: #2f4a2a;
    --sun: #f2b52a;
    --sun-deep: #e08a1c;
    --ruby: #9e1f1a;
    --ember: #d4521c;
    --teal: #1f9db5;
  }
  * { margin: 0; padding: 0; box-sizing: border-box; }
  html, body { width: 1200px; height: 1200px; overflow: hidden; }
  body {
    background: var(--backdrop);
    display: flex;
    align-items: center;
    justify-content: center;
    gap: 56px;
  }
  .label {
    position: relative;
    width: 292px;
    height: 480px;
    background: var(--paper);
    color: var(--ink);
    text-align: center;
    font-family: "Barlow Condensed", sans-serif;
  }
  .brand {
    position: absolute;
    top: 48px;
    left: 0;
    right: 0;
    font-family: "Playfair Display", serif;
    font-weight: 400;
    line-height: 1;
    z-index: 2;
  }
  .brand-main { display: block; font-size: 42px; letter-spacing: 1px; }
  .brand-sub { display: block; font-size: 19px; letter-spacing: 1px; margin-top: 2px; padding-left: 30px; }
  .range {
    position: absolute;
    top: 118px;
    right: 56px;
    font-size: 11px;
    letter-spacing: 2px;
    color: var(--ink-soft);
    z-index: 2;
  }
  .artwork { position: absolute; z-index: 1; }
  .artwork-green {
    left: 50px; top: 140px; width: 200px; height: 240px;
    background: radial-gradient(ellipse at 50% 45%, var(--leaf-deep) 0%, var(--leaf) 35%, rgba(170,190,120,0.35) 60%, rgba(247,247,245,0) 75%);
  }
  .artwork-red {
    left: 50px; top: 80px; width: 230px; height: 300px;
    background:
      radial-gradient(ellipse at 42% 45%, var(--ruby) 0%, var(--ember) 22%, rgba(224,138,28,0) 40%),
      linear-gradient(160deg, var(--sun) 0%, var(--sun-deep) 60%, var(--sun) 100%);
    clip-path: polygon(12% 8%, 100% 0%, 92% 40%, 82% 78%, 55% 96%, 22% 100%, 10% 70%, 0% 38%);
  }
  .artwork-blue {
    left: 44px; top: 144px; width: 204px; height: 216px;
    background:
      radial-gradient(ellipse at 52% 42%, #123440 0%, var(--teal) 20%, rgba(31,157,181,0) 38%),
      radial-gradient(ellipse at 20% 60%, var(--ember) 0%, rgba(212,82,28,0) 50%),
      linear-gradient(135deg, var(--sun-deep), var(--sun) 45%, #f6d36a 100%);
  }
  .details {
    position: absolute;
    left: 0; right: 0;
    top: 384px;
    z-index: 2;
    color: var(--ink);
  }
  .vintage { font-size: 14px; letter-spacing: 2px; font-weight: 500; }
  .origin { font-size: 9px; letter-spacing: 1.5px; margin-top: 3px; }
  .maker { font-size: 9px; letter-spacing: 1.5px; margin-top: 6px; line-height: 1.4; }
  .note { font-size: 5px; letter-spacing: 1px; margin-top: 8px; font-weight: 500; }
</style>
</head>
<body>
  <section class="label label-bianco">
    <h1 class="brand"><span class="brand-main">VALORA</span><span class="brand-sub">DI CASTEGNO</span></h1>
    <div class="range">BARREL SELECT</div>
    <div class="artwork artwork-green" role="img" aria-label="Painted green butterfly artwork in loose brushstrokes"></div>
    <div class="details">
      <p class="vintage">2018 BIANCO</p>
      <p class="origin">PIEMONTE / ITALY</p>
      <p class="maker">ARTISANLLY CRAFTED BY<br>CANTINA SETTE QUERCE</p>
      <p class="note">SUSTAINABLY FARMED</p>
    </div>
  </section>

  <section class="label label-rosso">
    <h1 class="brand"><span class="brand-main">VALORA</span><span class="brand-sub">DI CASTEGNO</span></h1>
    <div class="range">BARREL SELECT</div>
    <div class="artwork artwork-red" role="img" aria-label="Painted red butterfly on a yellow brushstroke splash"></div>
    <div class="details">
      <p class="vintage">2018 ROSSO</p>
      <p class="origin">PIEMONTE / ITALY</p>
      <p class="maker">ARTISANLLY CRAFTED BY<br>CANTINA SETTE QUERCE</p>
      <p class="note">SUSTAINABLY FARMED</p>
    </div>
  </section>

  <section class="label label-bianco-alt">
    <h1 class="brand"><span class="brand-main">VALORA</span><span class="brand-sub">DI CASTEGNO</span></h1>
    <div class="range">BARREL SELECT</div>
    <div class="artwork artwork-blue" role="img" aria-label="Painted blue butterfly on a square orange and yellow background"></div>
    <div class="details">
      <p class="vintage">2018 BIANCO</p>
      <p class="origin">PIEMONTE / ITALY</p>
      <p class="maker">ARTISANLLY CRAFTED BY<br>CANTINA SETTE QUERCE</p>
      <p class="note">SUSTAINABLY FARMED</p>
    </div>
  </section>
</body>
</html>
```